business card for Franco-Turkish restaurant

We are a Franco-Turkish restaurant, Le Mirandel, based in the Cotes d'Armor in Brittany, near the Pink Granite Coast. We serve mainly Turkish cuisine. We would like a card reminding Britain and Turkey. No flag. Color: turquoise (sea ..), green, red. There should be a space for 3 lines: name, address, phone / email

Industry/Entity Type

Fast Food Restaurant

Contact Information for Business Card

Dalbayrak Emrul
Addresse: 14 Rue Paul-Henri Duvic, 22450 Kervalhec, France
Tel:+33 2 96 47 08 39

Colors
33a6d7
f04a50
acd036

Requirements
Nice to have
• Symbols of Britain and Turkey
Should not have
• No flags

```html
<!DOCTYPE html>
<html lang="fr">
<head>
<meta charset="utf-8">
<title>Le Mirandel – Cartes de visite</title>
<link href="https://fonts.googleapis.com/css2?family=Crimson+Text:wght@400;600&display=swap" rel="stylesheet">
<style>
  :root {
    --backdrop: #ecebe8;
    --turquoise: #1f9aaa;
    --turquoise-deep: #17879a;
    --sea-blue: #33a6d7;
    --anatolia-red: #f04a50;
    --breton-green: #acd036;
    --paper: #f7f8f7;
    --ink-light: #ffffff;
    --card-shadow: rgba(0, 0, 0, 0.22);
  }
  * { margin: 0; padding: 0; box-sizing: border-box; }
  html, body {
    width: 1200px;
    height: 1023px;
    overflow: hidden;
    background: var(--backdrop);
    font-family: "Crimson Text", Georgia, serif;
  }
  .stage { position: relative; width: 1200px; height: 1023px; }
  .card {
    position: absolute;
    width: 540px;
    height: 309px;
    border-radius: 4px;
    background: var(--turquoise);
    box-shadow: 0 10px 28px var(--card-shadow);
    overflow: hidden;
  }
  .card--front { left: 60px; top: 150px; }
  .card--back  { left: 600px; top: 560px; }

  .frame { position: absolute; inset: 0; width: 540px; height: 309px; }
  .front-brand {
    position: absolute;
    inset: 0;
    display: flex;
    align-items: center;
    justify-content: center;
    gap: 26px;
  }
  .brand-dot {
    width: 108px;
    height: 108px;
    border-radius: 50%;
    background: var(--turquoise);
    box-shadow: 0 0 0 5px var(--paper), 0 0 0 7px var(--turquoise);
    flex: none;
  }
  .brand-text { display: flex; flex-direction: column; align-items: center; }
  .brand-name {
    font-size: 46px;
    font-weight: 400;
    line-height: 1;
    color: var(--turquoise);
  }
  .brand-tag {
    margin-top: 8px;
    font-size: 12px;
    letter-spacing: 4px;
    color: var(--turquoise);
  }
  .accent-rule {
    display: flex;
    gap: 6px;
    margin-top: 8px;
  }
  .accent-rule span { display: block; width: 34px; height: 3px; border-radius: 2px; }
  .accent-rule .rule--red { background: var(--anatolia-red); }
  .accent-rule .rule--sea { background: var(--sea-blue); }
  .accent-rule .rule--green { background: var(--breton-green); }

  .card--back {
    background: linear-gradient(160deg, var(--turquoise) 0%, var(--turquoise-deep) 100%);
    color: var(--ink-light);
  }
  .back-brand {
    position: absolute;
    left: 210px;
    top: 34px;
    display: flex;
    align-items: center;
    gap: 18px;
  }
  .back-brand .brand-dot {
    width: 88px;
    height: 88px;
    background: var(--ink-light);
    box-shadow: 0 0 0 4px var(--turquoise), 0 0 0 6px var(--ink-light);
  }
  .back-brand .brand-name { color: var(--ink-light); font-size: 34px; }
  .back-brand .brand-tag { color: var(--ink-light); font-size: 10px; letter-spacing: 3px; }
  .contact {
    position: absolute;
    left: 40px;
    top: 162px;
    list-style: none;
    font-size: 15px;
    line-height: 1.5;
  }
  .contact__name { font-size: 24px; font-weight: 600; margin-bottom: 4px; }
</style>
</head>
<body>
<main class="stage">

  <section class="card card--front" aria-label="Recto de la carte">
    <svg class="frame" viewBox="0 0 540 309" aria-hidden="true">
      <path d="M60 22 H480 V36 H498 V54 H518 V255 H498 V273 H480 V287 H60 V273 H42 V255 H22 V54 H42 V36 H60 Z" fill="#f7f8f7"/>
      <path d="M68 32 H472 V44 H490 V62 H508 V247 H490 V265 H472 V277 H68 V265 H50 V247 H32 V62 H50 V44 H68 Z" fill="none" stroke="#1f9aaa" stroke-width="1.5"/>
    </svg>
    <div class="front-brand">
      <span class="brand-dot"></span>
      <div class="brand-text">
        <span class="brand-name">Le Mirandel</span>
        <span class="brand-tag">RESTAURANT FRANCO-TURC</span>
        <div class="accent-rule" aria-hidden="true">
          <span class="rule--red"></span><span class="rule--sea"></span><span class="rule--green"></span>
        </div>
      </div>
    </div>
  </section>

  <section class="card card--back" aria-label="Verso de la carte">
    <div class="back-brand">
      <span class="brand-dot"></span>
      <div class="brand-text">
        <span class="brand-name">Le Mirandel</span>
        <span class="brand-tag">RESTAURANT FRANCO-TURC</span>
        <div class="accent-rule" aria-hidden="true">
          <span class="rule--red"></span><span class="rule--sea"></span><span class="rule--green"></span>
        </div>
      </div>
    </div>
    <ul class="contact">
      <li class="contact__name">Dalbayrak Emrul</li>
      <li class="contact__phone">+33 2 96 47 08 39</li>
      <li class="contact__email">contact@lemirandel-table.fr</li>
      <li class="contact__address">14 Rue Paul-Henri Duvic, 22450 Kervalhec</li>
    </ul>
  </section>

</main>
</body>
</html>
```